Brightwell Consulting Business Card Design

Business Card Design for Brightwell Consulting. Brightwell Consulting is a boutique consultancy based in Atlanta, GA., that specializes in marketing strategy, organization planning, and leadership development. We provide solutions for small businesses and startups as well as Summit 400 companies.

http://brightwellconsulting.example/

Target Market(s)

We provide solutions for small businesses and startups as well as Summit 400 companies.

Industry/Entity Type

Consulting

Contact Information for Business Card

Two sided business card with priority on contact information, logo, tag line (Inspiration to Dream More, Do More, Become More)

Colors

Designer to choose colors to be used in the design.

Requirements
Must have
• contact information, logo, tag line (Inspiration to Dream More, Do More, Become More)
• Simple no over communication.
Nice to have
• I would like to see different placements of logo and creative use of both sides of the card
Should not have
• Do not put too much information on the card.

```html
<!DOCTYPE html>
<html lang="en">
<head>
<meta charset="utf-8">
<title>Brightwell Consulting Business Card</title>
<link rel="stylesheet" href="https://fonts.googleapis.com/css2?family=Lato:wght@400;700&family=Niconne&display=swap">
<style>
  :root {
    --backdrop: #555555;
    --card-light: #ffffff;
    --card-dark: #333333;
    --ink: #2b2b2b;
    --ink-soft: #3a3a3a;
    --rule: #8a8fb0;
    --paper-text: #f4f4f4;
  }
  * { margin: 0; padding: 0; box-sizing: border-box; }
  html, body { width: 1200px; height: 900px; overflow: hidden; }
  body {
    background: var(--backdrop);
    position: relative;
    font-family: "Lato", Arial, sans-serif;
  }
  .card {
    position: absolute;
    top: 170px;
    width: 347px;
    height: 561px;
    text-align: center;
  }
  .card--front { left: 259px; background: var(--card-light); color: var(--ink); }
  .card--back { left: 631px; background: var(--card-dark); color: var(--paper-text); }

  .brand {
    position: absolute;
    top: 150px;
    left: 0; right: 0;
    font-weight: 700;
    color: var(--ink);
    letter-spacing: 3px;
    line-height: 1.1;
  }
  .brand__name { display: block; font-size: 36px; }
  .brand__sub { display: block; font-size: 19px; letter-spacing: 6px; margin-top: 4px; }

  .contact { position: absolute; top: 396px; left: 0; right: 0; }
  .contact__name { font-size: 20px; font-weight: 700; letter-spacing: 0.5px; color: var(--ink); }
  .contact__role { font-size: 14px; color: var(--ink-soft); margin-top: 2px; }
  .contact__rule { width: 157px; height: 1px; background: var(--rule); margin: 12px auto 12px; }
  .contact__line { font-size: 14px; color: var(--ink-soft); line-height: 21px; }
  .contact__line b { font-weight: 700; }
  .contact__web { font-weight: 700; color: var(--ink); }

  .tagline {
    position: absolute;
    top: 138px;
    left: 0; right: 0;
    font-family: "Niconne", cursive;
    font-size: 46px;
    line-height: 78px;
    color: var(--paper-text);
  }
  .back-web {
    position: absolute;
    top: 514px;
    left: 0; right: 0;
    font-size: 15px;
    letter-spacing: 1.8px;
    color: var(--paper-text);
  }
</style>
</head>
<body>
  <section class="card card--front">
    <div class="brand">
      <span class="brand__name">BRIGHTWELL</span>
      <span class="brand__sub">CONSULTING</span>
    </div>
    <div class="contact">
      <div class="contact__name">DANIEL MOREAU</div>
      <div class="contact__role">Managing Director</div>
      <div class="contact__rule"></div>
      <div class="contact__line"><b>P:</b> 555-014-7890</div>
      <div class="contact__line"><b>E:</b> info@brightwellmail.example</div>
      <div class="contact__line contact__web">www.brightwellconsulting.example</div>
    </div>
  </section>

  <section class="card card--back">
    <p class="tagline">Inspiration to<br>Dream More<br>Do More<br>Become More</p>
    <p class="back-web">www.brightwellconsulting.example</p>
  </section>
</body>
</html>
```